Plant Grower/Nursery needs a fun, professional and fresh 1/2 page print ad for a high profile gar...

We need a print ad for a garden tour geared towards plant enthusiasts that support California Native, natural and sustainable plants. A good percentage of our target market want a conservation and earth friendly approach to gardens/landscaping. We want to target this market, as well as, people who are looking for a pretty/colorful landscape that require little water/maintenance. **PLEASE LET US KNOW IF YOU HAVE QUESTIONS OR NEED MORE INFORMATION. WE ALSO HAVE MANY MORE PICTURES IF THESE DON'T WORK FOR YOUR DESIGN. ***THE AD CAN HAVE AS FEW AS 1 PHOTO - WE ARE POSTING SEVERAL IN HOPES THAT YOU CAN FIND WHAT IS PERFECT FOR YOUR IDEA!!Thank you

Target Market(s)

Gardeners, Landscapers, Landscape Designers/Architects, Cities and Municipalities.

Industry/Entity Type

Agriculture

Font styles to use
Serif
Sans Serif

Colors

Requirements
Must have
• We believe in growing regionally appropriate plants for Southern California that beatify our natural and urban landscapes.
• For over 20 years, our owners and staff take pride in providing timely, expert, and honest service.
Nice to have
• At least 1 photo. Eye catchy with a modern earthy feel.
• Hundreds of species/hybrids in stock of California Natives, Succulents, Ornamental Grasses, Standard Stock Items and Unique Plants.

```html
<!DOCTYPE html>
<html lang="en">
<head>
<meta charset="utf-8">
<title>Nursery Half Page Ad</title>
<link rel="stylesheet" href="https://fonts.googleapis.com/css2?family=Montserrat:wght@500&family=Roboto:wght@400;500&display=swap">
<style>
  :root {
    --brand-red: #7a150f;
    --slate: #464646;
    --divider: #ffffff;
    --succulent-light: #b3c7bd;
    --succulent-mid: #8ea79c;
    --succulent-dark: #6f7d80;
    --foliage-light: #5f9a3c;
    --foliage-dark: #1f4a1a;
    --bloom: #e08a12;
    --text-light: #ffffff;
  }
  html, body {
    margin: 0;
    padding: 0;
    width: 1200px;
    height: 903px;
    overflow: hidden;
    background: #ffffff;
  }
  .ad {
    position: relative;
    width: 1200px;
    height: 903px;
    overflow: hidden;
  }
  .ad-art {
    position: absolute;
    inset: 0;
    display: block;
  }
  .heritage-note {
    position: absolute;
    left: 42px;
    top: 38px;
    margin: 0;
    font-family: "Roboto", Arial, sans-serif;
    font-weight: 500;
    font-size: 29px;
    line-height: 40px;
    color: var(--text-light);
  }
  .heritage-note .lead {
    text-transform: uppercase;
    font-weight: 400;
  }
  .mission-note {
    position: absolute;
    left: 44px;
    top: 712px;
    margin: 0;
    font-family: "Montserrat", Arial, sans-serif;
    font-weight: 500;
    font-size: 28px;
    line-height: 40px;
    color: var(--text-light);
  }
</style>
</head>
<body>
<main class="ad">
  <svg class="ad-art" width="1200" height="903" viewBox="0 0 1200 903" xmlns="http://www.w3.org/2000/svg">
    <defs>
      <radialGradient id="succulentTone" cx="0.45" cy="0.55" r="0.75">
        <stop offset="0" stop-color="var(--succulent-light)"/>
        <stop offset="0.6" stop-color="var(--succulent-mid)"/>
        <stop offset="1" stop-color="var(--succulent-dark)"/>
      </radialGradient>
      <linearGradient id="foliageTone" x1="0" y1="0" x2="1" y2="1">
        <stop offset="0" stop-color="var(--foliage-light)"/>
        <stop offset="0.35" stop-color="var(--bloom)"/>
        <stop offset="0.6" stop-color="var(--foliage-dark)"/>
        <stop offset="0.8" stop-color="var(--bloom)"/>
        <stop offset="1" stop-color="var(--foliage-light)"/>
      </linearGradient>
    </defs>

    <rect class="photo-succulents" x="0" y="0" width="780" height="903" fill="url(#succulentTone)"
          role="img" aria-label="Photo of a dense bed of blue-green rosette succulents"/>

    <polygon class="photo-blooms" points="740,0 1200,0 1200,903 842,903 690,470" fill="url(#foliageTone)"
             role="img" aria-label="Photo of orange and red striped gazania flowers among green foliage"/>

    <polyline class="photo-divider" points="740,0 690,470 842,903" fill="none"
              stroke="var(--divider)" stroke-width="9" stroke-linejoin="miter"/>

    <polygon class="heritage-band" points="0,0 740,0 719,200 0,200" fill="var(--brand-red)"/>

    <polygon class="mission-band" points="0,672 760,672 842,903 0,903" fill="var(--slate)"/>
  </svg>

  <p class="heritage-note">
    <span class="lead">For over 20 years</span><br>
    our owners &amp; staff take pride in<br>
    providing timely, expert, &amp; honest service
  </p>

  <p class="mission-note">
    We believe in growing regionally appropriate<br>
    plants for Southern California that beatify<br>
    our natural and urban landscapes.
  </p>
</main>
</body>
</html>
```